Conceptual Model Diagram for Replacing Medication with Behavior to Support Weight Loss Maintenance

Design a figure of a conceptual model that needs to be inserted into a word document for a PSF grant. This conceptual model illustrates how behavioral strategies can replace the regulatory functions lost after AOM discontinuation. The intervention targets three core vulnerabilities—appetite resurgence, metabolic inflexibility, and suboptimal mindstate—through the domains of Food, Physical Activity, and Mind. Sustained weight loss maintenance occurs at the intersection of these domains. The intervention is delivered within a design framework that makes behaviors easier to perform, aligns them with identity, and reinforces them through virtual support and community, ensuring real-world feasibility and long-term adherence.
Target Market(s)
PSF reviewers
Industry/Entity Type
academic
Other font styles liked:
- arial
Requirements
Must have
- see my attached description

```html
<!DOCTYPE html>
<html lang="en">
<head>
<meta charset="utf-8">
<title>Sustained Weight Loss Maintenance – Conceptual Model</title>
<link rel="stylesheet" href="https://fonts.googleapis.com/css2?family=Archivo:wght@700;800&family=Roboto+Condensed:wght@800;900&display=swap">
<style>
  :root {
    --teal: #03bba6;
    --teal-deep: #02937f;
    --track-grey: #e7e7e7;
    --ink: #1d1d1b;
    --paper: #ffffff;
  }
  html, body {
    margin: 0;
    padding: 0;
    width: 1200px;
    height: 1198px;
    overflow: hidden;
    background: var(--paper);
  }
  .model {
    display: block;
    width: 1200px;
    height: 1198px;
  }
  .vulnerability-track { fill: none; stroke: var(--track-grey); stroke-width: 95; stroke-linecap: round; }
  .vulnerability-label {
    font-family: "Archivo", Arial, sans-serif;
    font-weight: 800;
    font-size: 50px;
    fill: var(--ink);
  }
  .domain-ring { fill: var(--teal); }
  .domain-node { fill: var(--teal); }
  .domain-node-shadow { fill: var(--teal-deep); opacity: .55; }
  .domain-label {
    font-family: "Roboto Condensed", Arial, sans-serif;
    font-weight: 900;
    fill: var(--paper);
  }
  .domain-label--big { font-size: 96px; }
  .domain-label--long { font-size: 80px; }
  .icon-badge { fill: var(--paper); }
  .core-disc { fill: var(--paper); }
  .core-title {
    font-family: "Roboto Condensed", Arial, sans-serif;
    font-weight: 900;
    fill: var(--ink);
    text-anchor: middle;
  }
  .core-title--small { font-size: 66px; }
  .core-title--large { font-size: 150px; }
</style>
</head>
<body>
<svg class="model" viewBox="0 0 1920 1917" preserveAspectRatio="none" xmlns="http://www.w3.org/2000/svg">
  <defs>
    <path id="arc-appetite" d="M872 422 A552 552 0 0 1 1520 966"/>
    <path id="arc-metabolic" d="M489 667 A565 565 0 0 0 686 1455"/>
    <path id="arc-mindstate" d="M819 1521 A575 575 0 0 0 1534 1066"/>
    <path id="arc-food" d="M968 631 A335 335 0 0 1 1258 798"/>
    <path id="arc-activity" d="M626 769 A395 395 0 0 0 770 1308"/>
    <path id="arc-mind" d="M1070 1348 A395 395 0 0 0 1326 1133"/>
    <radialGradient id="ring-shade" cx="50%" cy="50%" r="50%">
      <stop offset="60%" stop-color="#03bba6"/>
      <stop offset="100%" stop-color="#04b3a0"/>
    </radialGradient>
  </defs>

  <!-- Outer vulnerabilities -->
  <g class="vulnerabilities">
    <path class="vulnerability-track" d="M666 483 A570 570 0 0 1 1529 867"/>
    <path class="vulnerability-track" d="M538 592 A570 570 0 0 0 701 1469"/>
    <path class="vulnerability-track" d="M1529 1065 A570 570 0 0 1 898 1532"/>

    <text class="vulnerability-label"><textPath href="#arc-appetite" startOffset="38" textLength="710" lengthAdjust="spacing">APPETITE RESURGENCE</textPath></text>
    <text class="vulnerability-label"><textPath href="#arc-metabolic" startOffset="138" textLength="651" lengthAdjust="spacing">METABOLIC INFLEXIBILITY</textPath></text>
    <text class="vulnerability-label"><textPath href="#arc-mindstate" startOffset="201" textLength="622" lengthAdjust="spacing">SUBOPTIMAL MINDSTATE</textPath></text>
  </g>

  <!-- Intervention domains -->
  <g class="domains">
    <circle class="domain-ring" cx="968" cy="966" r="494" fill="url(#ring-shade)"/>

    <circle class="domain-node-shadow" cx="735" cy="672" r="128"/>
    <circle class="domain-node" cx="722" cy="660" r="122"/>
    <circle class="domain-node-shadow" cx="1352" cy="998" r="128"/>
    <circle class="domain-node" cx="1365" cy="985" r="122"/>
    <circle class="domain-node-shadow" cx="874" cy="1352" r="128"/>
    <circle class="domain-node" cx="860" cy="1340" r="122"/>

    <text class="domain-label domain-label--big"><textPath href="#arc-food" startOffset="58" textLength="175" lengthAdjust="spacingAndGlyphs">FOOD</textPath></text>
    <text class="domain-label domain-label--long"><textPath href="#arc-activity" startOffset="34" textLength="551" lengthAdjust="spacingAndGlyphs">PHYSICAL ACTIVITY</textPath></text>
    <text class="domain-label domain-label--big"><textPath href="#arc-mind" startOffset="62" textLength="200" lengthAdjust="spacingAndGlyphs">MIND</textPath></text>

    <circle class="icon-badge" cx="722" cy="660" r="77" role="img" aria-label="Food icon: milk carton, apple and carrot"/>
    <circle class="icon-badge" cx="1365" cy="985" r="77" role="img" aria-label="Mind icon: brain"/>
    <circle class="icon-badge" cx="860" cy="1340" r="77" role="img" aria-label="Physical activity icon: person lifting dumbbells"/>
  </g>

  <!-- Core outcome -->
  <g class="outcome">
    <circle class="core-disc" cx="969" cy="964" r="289"/>
    <text class="core-title core-title--small" x="975" y="830" textLength="282" lengthAdjust="spacingAndGlyphs">SUSTAINED</text>
    <text class="core-title core-title--large" x="976" y="946" textLength="424" lengthAdjust="spacingAndGlyphs">WEIGHT</text>
    <text class="core-title core-title--large" x="976" y="1068" textLength="264" lengthAdjust="spacingAndGlyphs">LOSS</text>
    <text class="core-title core-title--small" x="976" y="1138" textLength="373" lengthAdjust="spacingAndGlyphs">MAINTENANCE</text>
  </g>
</svg>
</body>
</html>
```